New Business Card Design Project

We require a business card design for Zelvaquin, a newly established Indian company.
Our focus is on the development, manufacturing, and export of a diverse array of pharmaceutical products on a global scale. The card should convey a professional appearance, as our primary markets are in Africa, China, and Southeast Asian nations.
We envision a two-sided business card, with the reverse side dedicated to a logo set against a solid color or an elegantly designed pattern. The corners should be rounded. We would appreciate seeing both horizontal and vertical design options. We trust the designer to utilize their expertise in creating this design.

The content for the business card is included in the attached Word file.

Target Market(s)

Our primary markets are in Africa, China, and Southeast Asian, Latin America, Maldives, Sri Lanka

Industry/Entity Type

Pharmaceutical Manufacturing and Export

Contact Information for Business Card

Colors

Designer to choose colors to be used in the design.

Requirements
Must have
• The reverse side of the business card features solely the logo along with the tagline, "Remedies of Life."
Should not have
• The logo should not exceed two instances, encompassing both the front and back sides of the card.

```html
<!DOCTYPE html>
<html lang="en">
<head>
<meta charset="utf-8">
<title>Zelvaquin business cards</title>
<link href="https://fonts.googleapis.com/css2?family=Montserrat:wght@400;500;700;800&display=swap" rel="stylesheet">
<style>
  :root {
    --bg: #d4d3cf;
    --card: #ffffff;
    --blue: #29a8e0;
    --red: #f0604c;
    --ink: #1d1d1d;
  }
  * { margin: 0; padding: 0; box-sizing: border-box; }
  html, body { width: 1200px; height: 801px; overflow: hidden; }
  body {
    background: var(--bg);
    font-family: "Montserrat", sans-serif;
    position: relative;
  }
  .card {
    position: absolute;
    width: 525px;
    height: 300px;
    background: var(--card);
    border-radius: 14px;
    box-shadow: 0 10px 30px rgba(0,0,0,0.18);
    overflow: hidden;
  }
  .card-front { left: 50px; top: 250px; }
  .card-back { left: 625px; top: 250px; }

  .front-brand {
    position: absolute;
    left: 0; top: 0;
    width: 250px; height: 272px;
    display: flex; align-items: center; justify-content: center; gap: 10px;
  }
  .brand-dot {
    width: 18px; height: 18px; border-radius: 50%;
    background: var(--red);
    flex: none;
  }
  .brand-name {
    color: var(--blue);
    font-weight: 800;
    font-size: 32px;
    letter-spacing: -0.5px;
    white-space: nowrap;
  }
  .divider {
    position: absolute;
    left: 250px; top: 40px;
    width: 1px; height: 190px;
    background: var(--blue);
  }
  .contact {
    position: absolute;
    left: 272px; top: 38px;
    color: var(--ink);
    font-size: 12.5px;
    line-height: 1.35;
  }
  .person-name {
    color: var(--blue);
    font-weight: 800;
    font-size: 19px;
    margin-bottom: 2px;
  }
  .person-role, .person-company { font-weight: 400; }
  .contact-list { list-style: none; margin-top: 14px; }
  .contact-list li { display: flex; align-items: center; gap: 6px; }
  .contact-list svg { width: 12px; height: 12px; flex: none; }
  .address { margin-top: 14px; }

  .edge-band {
    position: absolute;
    left: 0; bottom: 0;
    width: 525px; height: 28px;
  }

  .back-brand {
    position: absolute;
    inset: 0;
    display: flex; flex-direction: column; align-items: center; justify-content: center; gap: 8px;
  }
  .back-lockup { display: flex; align-items: center; gap: 14px; }
  .back-brand .brand-name { font-size: 56px; }
  .back-brand .brand-dot { width: 28px; height: 28px; }
  .tagline {
    color: var(--red);
    font-weight: 500;
    font-size: 16px;
    letter-spacing: 3px;
    text-transform: uppercase;
  }
</style>
</head>
<body>

<section class="card card-front">
  <div class="front-brand">
    <span class="brand-dot"></span>
    <span class="brand-name">Zelvaquin</span>
  </div>
  <div class="divider"></div>
  <div class="contact">
    <p class="person-name">Arvind K. Solanke</p>
    <p class="person-role">CEO</p>
    <p class="person-company">Zelvaquin</p>
    <ul class="contact-list">
      <li>
        <svg viewBox="0 0 12 12"><path d="M2.5 1h2l1 3-1.3 1a6.5 6.5 0 0 0 2.8 2.8L8 6.5l3 1v2c0 .8-.7 1.5-1.5 1.5A8.5 8.5 0 0 1 1 2.5C1 1.7 1.7 1 2.5 1z" fill="var(--blue)"/></svg>
        +919812305471
      </li>
      <li>
        <svg viewBox="0 0 12 12"><rect x="0.5" y="2" width="11" height="8" rx="1" fill="var(--red)"/><path d="M1 2.5l5 4 5-4" fill="none" stroke="#fff" stroke-width="1"/></svg>
        asolanke@zelvaquin.com
      </li>
      <li>
        <svg viewBox="0 0 12 12"><circle cx="6" cy="6" r="5.3" fill="var(--blue)"/><path d="M0.8 6h10.4M6 0.8c-2.5 3-2.5 7.4 0 10.4M6 0.8c2.5 3 2.5 7.4 0 10.4" fill="none" stroke="#fff" stroke-width="0.8"/></svg>
        www.zelvaquin.com
      </li>
    </ul>
    <p class="address">12, Kesar Vihar Colony,<br>Ramtekpur, 440217, India</p>
  </div>
  <svg class="edge-band" viewBox="0 0 525 28" preserveAspectRatio="none">
    <rect x="0" y="0" width="525" height="28" fill="var(--blue)"/>
    <path d="M322 0H525V28H312C304 20 308 6 322 0Z" fill="var(--red)"/>
  </svg>
</section>

<section class="card card-back">
  <div class="back-brand">
    <div class="back-lockup">
      <span class="brand-dot"></span>
      <span class="brand-name">Zelvaquin</span>
    </div>
    <p class="tagline">Remedies of Life</p>
  </div>
</section>

</body>
</html>
```